Postcard Design Project A Healthy reminder

Dr.'s Jeetesh and Lorna sethi. Internal Medicine/Family practice. This postcard will be for our patients that we have not seen in a while. Also we need another postcard (the one your designing) with a different heading for New patient's. Do you offer a price break for that? The only thing we would need to change is the heading. Please let me know. Thank you so much! Also can you use the map on the last postcard and our logo I made? I cant find it. Please feel free to call me or email me.

```html
<!DOCTYPE html>
<html lang="en">
<head>
<meta charset="utf-8">
<title>A Healthy Reminder – Postcard</title>
<link href="https://fonts.googleapis.com/css2?family=Barlow:wght@800&family=Barlow+Semi+Condensed:wght@300&family=Lato:wght@400;700;900&display=swap" rel="stylesheet">
<style>
  :root{
    --maroon:#8b1a1f;
    --ink:#2b2b2b;
    --grey-dark:#3a3b3d;
    --grey-light:#a6a7a9;
    --stripe:#6f7072;
    --stripe-light:#b4b4b4;
    --white:#ffffff;
  }
  *{box-sizing:border-box;margin:0;padding:0}
  html,body{width:926px;height:1200px;overflow:hidden}
  body{
    position:relative;
    background:linear-gradient(to bottom,var(--grey-dark) 0 876px,var(--grey-light) 876px 100%);
    font-family:"Lato",sans-serif;color:var(--ink);
  }
  .card{
    position:absolute;left:70px;width:786px;height:524px;overflow:hidden;
    background:linear-gradient(to right,#f1f1f1 0,#fff 8%,#fff 70%,#e9e9e9 100%);
    box-shadow:0 4px 10px rgba(0,0,0,.45);
  }
  .card--front{top:62px}
  .card--back{top:614px}
  .card svg.shapes{position:absolute;inset:0}

  /* front */
  .headline{position:absolute;left:34px;top:34px;font-family:"Barlow",sans-serif;font-weight:800;
    color:var(--maroon);font-size:87px;line-height:75px;letter-spacing:-1px}
  .subhead{position:absolute;left:34px;top:180px;font-family:"Barlow Semi Condensed",sans-serif;font-weight:300;
    font-size:49px;line-height:40px;color:var(--ink);letter-spacing:-1.5px}
  .values{position:absolute;left:16px;top:272px;width:470px;height:152px;background:var(--maroon);color:#fff}
  .value{position:absolute;left:66px;width:262px;font-size:11px;line-height:14px}
  .value strong{display:block;font-weight:700;font-size:11.5px}
  .value--1{top:9px}.value--2{top:63px}.value--3{top:103px}
  .value-rule{position:absolute;left:66px;width:256px;height:1.5px;background:#fff}
  .value-icon{position:absolute;left:18px;width:34px;height:34px}
  .front-contact{position:absolute;left:34px;top:434px;color:var(--maroon);font-weight:900}
  .front-contact .phone{font-size:28px;line-height:31px}
  .front-contact .web{font-size:28.5px;line-height:31px}
  .badge{position:absolute;left:352px;top:246px;width:204px;height:204px;border-radius:50%;
    background:var(--stripe);display:flex;align-items:center;justify-content:center}
  .badge-inner{width:188px;height:188px;border-radius:50%;background:#fff;border:2px solid #d4d4d4;
    display:flex;align-items:center;justify-content:center}
  .practice-name{font-family:"Lato",sans-serif;font-weight:700;color:var(--ink);font-size:15.5px;text-align:center}

  /* back */
  .back-name{position:absolute;left:20px;top:75px;width:300px;text-align:center;font-size:19px}
  .back-contact{position:absolute;left:31px;top:426px;color:#fff}
  .back-contact .address{font-weight:700;font-size:14px}
  .back-contact .phone{font-weight:700;font-size:33px;line-height:38px}
  .back-contact .web{font-size:16px;letter-spacing:5.6px;font-weight:700}
  .stamp{position:absolute;left:654px;top:32px;width:100px;height:99px;border:1.5px solid #555}
  .address-line{position:absolute;left:456px;width:298px;height:1.5px;background:#555}
</style>
</head>
<body>

<section class="card card--front">
  <svg class="shapes" width="786" height="524" viewBox="0 0 786 524">
    <defs>
      <linearGradient id="photoTone" x1="0" y1="0" x2="0" y2="1">
        <stop offset="0" stop-color="#c6a78c"/>
        <stop offset="0.25" stop-color="#e3d6c8"/>
        <stop offset="0.5" stop-color="#f3f1ee"/>
        <stop offset="0.72" stop-color="#d9dcdc"/>
        <stop offset="1" stop-color="#9ea7aa"/>
      </linearGradient>
      <linearGradient id="photoShade" x1="0" y1="0" x2="1" y2="0">
        <stop offset="0" stop-color="#8a6a55" stop-opacity=".35"/>
        <stop offset="0.45" stop-color="#ffffff" stop-opacity="0"/>
        <stop offset="1" stop-color="#6c6f72" stop-opacity=".3"/>
      </linearGradient>
    </defs>
    <path d="M503,0 C558,80 518,220 478,300 C438,380 428,460 498,524" fill="none" stroke="var(--stripe-light)" stroke-width="4"/>
    <path d="M515,0 C570,80 530,220 490,300 C450,380 440,460 510,524" fill="none" stroke="var(--stripe)" stroke-width="9"/>
    <path d="M529,0 C584,80 544,220 504,300 C464,380 454,460 524,524 L786,524 L786,0 Z" fill="var(--maroon)"/>
    <g role="img" aria-label="Photograph of two doctors in white coats reviewing a patient chart in a clinic hallway">
      <path d="M545,0 C600,80 560,220 520,300 C480,380 470,460 540,524 L786,524 L786,0 Z" fill="url(#photoTone)"/>
      <path d="M545,0 C600,80 560,220 520,300 C480,380 470,460 540,524 L786,524 L786,0 Z" fill="url(#photoShade)"/>
    </g>
  </svg>

  <h1 class="headline">A HEALTHY<br>REMINDER</h1>
  <p class="subhead">IT IS TIME FOR YOUR<br>ANNUAL EXAMS</p>

  <div class="values">
    <svg class="value-icon" style="top:12px" viewBox="0 0 34 34" fill="none" stroke="#fff" stroke-width="1.6">
      <ellipse cx="17" cy="17" rx="15" ry="6"/>
      <ellipse cx="17" cy="17" rx="15" ry="6" transform="rotate(60 17 17)"/>
      <ellipse cx="17" cy="17" rx="15" ry="6" transform="rotate(120 17 17)"/>
      <circle cx="17" cy="17" r="2.2" fill="#fff"/>
    </svg>
    <div class="value value--1"><strong>Experienced</strong>Over 20 years of experience practicing in primary<br>care and internal medicine.</div>
    <div class="value-rule" style="top:55px"></div>
    <svg class="value-icon" style="top:61px" viewBox="0 0 34 34" fill="none" stroke="#fff" stroke-width="1.8">
      <circle cx="17" cy="17" r="15"/>
      <path d="M10 17.5 L15 22.5 L24 12"/>
    </svg>
    <div class="value value--2"><strong>Professional</strong>We maintain exceptional standards of patient care.</div>
    <div class="value-rule" style="top:95px"></div>
    <svg class="value-icon" style="top:106px" viewBox="0 0 34 34" fill="none" stroke="#fff" stroke-width="1.8">
      <path d="M17 30 C8 22 2 17 2 10.5 C2 6 5.5 3 9.5 3 C13 3 15.5 5 17 8 C18.5 5 21 3 24.5 3 C28.5 3 32 6 32 10.5 C32 17 26 22 17 30 Z"/>
    </svg>
    <div class="value value--3"><strong>Compassionate</strong>Commited to providing quality healthcare to<br>our patients we are privileged to serve.</div>
  </div>

  <div class="badge"><div class="badge-inner"><span class="practice-name">Jeetesh T Sethi, M.D.</span></div></div>

  <div class="front-contact">
    <p class="phone">Office (559) 555-0142</p>
    <p class="web">www.jeeteshtsethimd.com</p>
  </div>
</section>

<section class="card card--back">
  <svg class="shapes" width="786" height="524" viewBox="0 0 786 524">
    <defs>
      <clipPath id="leftOfCurve">
        <path d="M0,0 L330,0 C282,120 412,300 392,420 C384,480 360,510 350,524 L0,524 Z"/>
      </clipPath>
      <linearGradient id="mapTone" x1="0" y1="0.3" x2="1" y2="0.7">
        <stop offset="0" stop-color="#eef0ea"/>
        <stop offset="0.5" stop-color="#f1efe6"/>
        <stop offset="0.72" stop-color="#d8e6cf"/>
        <stop offset="1" stop-color="#b7d3a6"/>
      </linearGradient>
    </defs>
    <path d="M380,0 C332,120 462,300 442,420 C434,480 410,510 400,524" fill="none" stroke="var(--stripe-light)" stroke-width="4"/>
    <path d="M366,0 C318,120 448,300 428,420 C420,480 396,510 386,524" fill="none" stroke="var(--stripe)" stroke-width="10"/>
    <path d="M348,0 C300,120 430,300 410,420 C402,480 378,510 368,524" fill="none" stroke="var(--maroon)" stroke-width="22"/>
    <g clip-path="url(#leftOfCurve)">
      <rect x="0" y="178" width="786" height="4" fill="var(--maroon)"/>
      <rect x="0" y="182" width="786" height="229" fill="url(#mapTone)"
        role="img" aria-label="Road map of the Fresno and Clovis area with a pin marking the office"/>
      <rect x="0" y="411" width="786" height="113" fill="var(--maroon)"/>
    </g>
    <g transform="translate(183,286)">
      <path d="M0,14 C-6,5 -9,1 -9,-5 A9,9 0 0 1 9,-5 C9,1 6,5 0,14 Z" fill="#d93a33"/>
      <circle cx="0" cy="-5" r="3.2" fill="#fff"/>
    </g>
  </svg>

  <p class="practice-name back-name">Jeetesh T Sethi, M.D.</p>

  <div class="back-contact">
    <p class="address">4820 N. Cedar Avenue Suite 210, Fresno, Ca 93726</p>
    <p class="phone">Office (559) 555-0142</p>
    <p class="web">www.jeeteshtsethimd.com</p>
  </div>

  <div class="stamp"></div>
  <div class="address-line" style="top:350px"></div>
  <div class="address-line" style="top:402px"></div>
  <div class="address-line" style="top:456px"></div>
</section>

</body>
</html>
```